WP website design (Whitcombe)

We need a wordpress design for an established auction and real estate company based in Daswon Creek, Canada. The winning design will incorporate a professional color scheme with company logo in a clean layout with specified widgets. The design needs to consider that this will be developed on a responsive theme. Colors will complement logo - red, black and gray.

Industry/Entity Type

Real Estate

Font styles to use
Sans Serif

Requirements
Must have
• Must Have:
the main logo is provided and the 'horse' logo shouldbe incorporated into the hearder or sidebar (either left or right)as well. Contact info should be placed in the header, and footer too: (250) 555-0147
(250) 555-0193
(250) 555-0128
lkr@fernvale-mail.example

- Navigation:
1) Home 2) Auctions 3) Online Auctions 4) About Us 5) Contact Us

Home Page will have following:
"Family owned and operated with a family guarantee.
Located in Dawson Creek, B.C. Canada

Competitive Rates Bonded & Licensed Livestock Dealers & Auctioneers
All Types of Auction Sales in B.C. & Alberta

Farm, Machinery
Equipment Sales
Household & Estate Sales
Livestock Marketing Consultants
Field Cattle Sales
Livestock Pedigree Sales
Horse Sales Appraisals"

Homepage will have auctions - as at http://brindlegatesales.example/upcoming-auctions/.

Footer will have smaller company logo, credit card logo, and attached association logos and this contact info:
.(620) 555-0176: OFFICE
(620) 555-0134: FAX
vgroup@tqx.example: email
Address: 718 N. Birch Rd., Johnson KS
Mailing Address: PO Box 829, Johnson, KS

Widgets:
1) email sign up 2) News blog widget 3) testimonial blog widget 4) featured auctions widget 5) the 'Gavel Row' logo which is included
Nice to have
• Nice to Have:
- demonstrate the drop-down menu styling, e.g. under Auctions
- Upcoming Auctions
- Past Auctions

```html
<!DOCTYPE html>
<html lang="en">
<head>
<meta charset="utf-8">
<title>Whitcombe's Auction Mart Ltd.</title>
<link rel="stylesheet" href="https://fonts.googleapis.com/css2?family=Open+Sans:wght@400;600;700&family=Arimo:ital,wght@0,400;0,700;1,400;1,700&display=swap">
<style>
:root{
  --red:#dd0a0a;
  --dark:#333333;
  --footer:#2b2b2b;
  --panel:#f1f1f1;
  --line:#d9d9d9;
  --text:#222222;
  --navy:#1d2f7a;
  --white:#ffffff;
}
*{box-sizing:border-box;margin:0;padding:0}
html,body{width:1142px;height:1200px;overflow:hidden;background:var(--white)}
.stage{position:relative;width:1200px;height:1261px;transform:scale(0.95167);transform-origin:0 0;font-family:"Arimo",Arial,sans-serif;color:var(--text)}
.abs{position:absolute}
.site-footer-band{left:0;top:1105px;width:1200px;height:156px;background:var(--footer)}
.page{left:110px;top:0;width:980px;height:1143px;background:var(--white);box-shadow:0 0 14px rgba(0,0,0,.35)}
.brand{left:130px;top:22px;width:160px;text-align:center;font-family:"Open Sans",sans-serif;font-weight:700;font-size:15px;line-height:24px;color:#111;white-space:nowrap}
.brand-dot{display:block;margin:8px auto 0;width:18px;height:18px;border-radius:50%;background:var(--red)}
.social-label{left:796px;top:52px;font-family:"Open Sans",sans-serif;font-size:22px;letter-spacing:1.5px;color:#333;white-space:nowrap}
.social{top:52px;width:30px;height:30px;border-radius:5px}
.nav{left:115px;top:116px;width:968px;height:41px;background:var(--red);display:flex;font-family:"Open Sans",sans-serif;font-size:14px;color:var(--white);letter-spacing:.6px}
.nav a{color:inherit;text-decoration:none;display:flex;align-items:center;justify-content:center;border-right:1px solid #b50000;height:100%;white-space:nowrap}
.hero{left:115px;top:157px;width:701px;height:318px;background:linear-gradient(180deg,#9db3cf 0%,#b8c4cf 35%,#8a6a55 55%,#6d7d4c 80%,#5f7b36 100%)}
.dot{top:451px;width:12px;height:12px;border-radius:50%;background:#444;border:2px solid #eee}
.dot.on{top:448px;width:18px;height:18px;background:var(--red)}
.signup{left:816px;top:157px;width:266px;height:318px;background:var(--dark);color:var(--white);font-family:"Open Sans",sans-serif}
.signup h2{position:absolute;left:26px;top:18px;font-weight:400;font-size:25px;letter-spacing:1px;white-space:nowrap}
.signup h2 span{display:inline-block;margin-left:4px;padding:0 10px;background:#eee;color:#333;border-radius:5px;line-height:29px}
.signup label{position:absolute;left:26px;font-size:13px;font-weight:600;letter-spacing:.5px}
.signup .field{position:absolute;left:27px;width:204px;height:28px;background:var(--white)}
.btn-subscribe{left:137px;top:266px;width:94px;height:30px;background:var(--red);color:var(--white);font-size:14px;letter-spacing:.6px;display:flex;align-items:center;justify-content:center}
.auctions{left:117px;top:499px;width:654px;height:632px;background:var(--panel);border:1px solid var(--line)}
.bar-head{height:37px;background:var(--red);color:var(--white);font-family:"Open Sans",sans-serif;font-size:21px;letter-spacing:.8px;padding:5px 0 0 9px}
.item{left:0;width:654px;height:187px}
.item-title{left:7px;top:0;font-family:"Open Sans",sans-serif;font-weight:400;font-size:15px;line-height:18px;letter-spacing:1.3px;color:#222;white-space:nowrap}
.thumb{left:8px;top:30px;width:167px;height:126px;background:var(--white);border:1px solid var(--line);padding:3px}
.thumb div{width:100%;height:100%;background:linear-gradient(160deg,#b7cde4 0%,#c7b071 45%,#8d7a55 75%,#6e7b5e 100%)}
.live{left:183px;top:31px;font-family:"Open Sans",sans-serif;font-size:14px;line-height:18px;color:var(--red);letter-spacing:.5px;white-space:nowrap}
.meta{left:183px;font-size:12.5px;line-height:16px;color:#222;white-space:nowrap}
.meta b{margin-right:6px}
.desc{left:183px;top:95px;width:296px;font-size:12px;line-height:14.5px;text-align:justify;color:#222}
.links{left:493px;top:32px;width:153px;height:94px;background:var(--white);border:1px solid var(--line)}
.link-row{position:absolute;left:6px;width:139px;height:40px;display:flex;align-items:center;gap:8px;font-size:13px;font-weight:700;color:#333;letter-spacing:.3px;white-space:nowrap}
.link-row + .link-row{border-top:1px solid var(--line)}
.rule{left:8px;top:170px;width:636px;border-top:1px dashed #bbb}
.view-more{left:574px;top:596px;width:73px;height:23px;border-radius:5px;background:var(--dark);color:var(--white);font-size:12px;font-style:italic;display:flex;align-items:center;justify-content:center}
.widget{left:815px;width:266px;background:#f4f4f4;border:1px solid var(--line)}
.widget-head{height:37px;background:var(--dark);color:var(--white);font-family:"Open Sans",sans-serif;font-size:21px;letter-spacing:.9px;padding:5px 0 0 11px;white-space:nowrap}
.read-more{position:absolute;right:11px;width:73px;height:23px;border-radius:6px;background:var(--red);color:var(--white);font-size:12px;font-style:italic;font-weight:700;display:flex;align-items:center;justify-content:center}
.fa-link{left:11px;top:48px;font-family:"Open Sans",sans-serif;font-size:12.5px;letter-spacing:1px;color:var(--navy);text-decoration:underline;white-space:nowrap}
.fa-thumb{left:11px;top:75px;width:108px;height:68px;background:linear-gradient(160deg,#b7cde4 0%,#c7b071 50%,#7f7a60 100%)}
.fa-text{left:126px;top:76px;font-size:12px;line-height:14px;color:#111;white-space:nowrap}
.video{left:1px;top:38px;width:263px;height:157px;background:linear-gradient(180deg,#a3b6cd 0%,#c9c3bb 30%,#8a5e4c 60%,#5d6f3a 100%)}
.play{left:102px;top:39px;width:60px;height:42px;border-radius:6px;background:rgba(20,20,20,.85)}
.controls{left:0;bottom:0;width:263px;height:24px;background:#111;color:#ddd;font-size:10px;display:flex;align-items:center;gap:8px;padding:0 8px}
.progress{width:80px;height:4px;background:#555;border-radius:2px}
.testimonial{left:12px;top:44px;width:246px;font-size:12.5px;line-height:18px;color:#111}
.footer-nav{left:120px;top:1176px;font-size:13px;color:var(--white);word-spacing:1px;white-space:nowrap}
.footer-nav span{margin:0 8px}
.copyright{left:119px;top:1200px;font-size:13px;color:var(--white);white-space:nowrap}
.horse{left:664px;top:1155px;width:46px;height:92px;background:linear-gradient(180deg,#555,#111);border-radius:14px 10px 6px 6px}
.foot-brand{left:740px;top:1164px;width:128px;text-align:center;font-family:"Open Sans",sans-serif;font-weight:700;font-size:12px;line-height:20px;color:var(--white);white-space:nowrap}
.foot-brand i{display:block;margin:6px auto 0;width:14px;height:14px;border-radius:50%;background:#ccc}
.card{top:1189px;height:25px;border-radius:2px;border:2px solid #ddd}
</style>
</head>
<body>
<div class="stage">
  <div class="abs site-footer-band"></div>
  <div class="abs page"></div>

  <header>
    <div class="abs brand">WHITCOMBE'S AUCTION<br>MART LTD.<span class="brand-dot"></span></div>
    <div class="abs social-label">Social media</div>
    <span class="abs social" style="left:958px;background:#3b5b9a"></span>
    <span class="abs social" style="left:995px;background:#1a8fbf"></span>
    <span class="abs social" style="left:1032px;background:#37b9e4"></span>
  </header>

  <nav class="abs nav">
    <a href="#" style="width:132px">HOME</a>
    <a href="#" style="width:130px">AUCTIONS</a>
    <a href="#" style="width:221px">REAL ESTATE LISTINGS</a>
    <a href="#" style="width:142px">ABOUT US</a>
    <a href="#" style="width:156px;border-right:none">CONTACT US</a>
  </nav>

  <section class="abs hero" role="img" aria-label="Large brick country house with turrets on a green lawn"></section>
  <span class="abs dot" style="left:132px"></span>
  <span class="abs dot" style="left:150px"></span>
  <span class="abs dot on" style="left:167px"></span>
  <span class="abs dot" style="left:189px"></span>

  <aside class="abs signup">
    <h2>EMAIL<span>SIGN UP</span></h2>
    <label style="top:68px">First Name</label>
    <div class="field" style="top:93px"></div>
    <label style="top:128px">Last Name</label>
    <div class="field" style="top:153px"></div>
    <label style="top:196px">Email Address</label>
    <div class="field" style="top:219px"></div>
    <div class="abs btn-subscribe">Subscribe</div>
  </aside>

  <main class="abs auctions">
    <div class="bar-head">Featured Auctions</div>

    <article class="abs item" style="top:53px">
      <h3 class="abs item-title">SHOP EQUIPMENT/TOOLS * PORK PROCESSING ITEMS</h3>
      <div class="abs thumb"><div role="img" aria-label="Yellow crawler loader tractor"></div></div>
      <div class="abs live">LIVE ON-SITE AUCTION</div>
      <div class="abs meta" style="top:51px"><b>Begins:</b> Saturday, March 16, 2013 at 10:00 AM EDT</div>
      <div class="abs meta" style="top:71px"><b>Location:</b> 5183 Larkin Road Fenwick, KY 40011</div>
      <p class="abs desc">Kestrel BS3F High Lift, 600 Series Halden tractor w/Brantley Loader, Dune buggy, 1207 RM Cutditioner: SHOP &amp; MISCELLANIOUS &amp; PORK PROCESSING ITEMS.</p>
      <div class="abs links">
        <div class="link-row" style="top:3px"><svg width="24" height="22" viewBox="0 0 24 22"><rect x="1" y="2" width="22" height="19" fill="#fff" stroke="#5a8fc8" stroke-width="1.5"/><rect x="1" y="2" width="22" height="5" fill="#5a8fc8"/><path d="M4 10h16M4 14h16M4 18h16M9 7v14M15 7v14" stroke="#9bbde0"/></svg>Details</div>
        <div class="link-row" style="top:46px"><svg width="24" height="22" viewBox="0 0 24 22"><rect x="1" y="6" width="22" height="15" rx="2" fill="#2a2f3a"/><rect x="7" y="2" width="9" height="5" fill="#2a2f3a"/><circle cx="12" cy="13" r="5" fill="#3f7fc0" stroke="#ccc"/></svg>Photo Galleries</div>
      </div>
      <div class="abs rule"></div>
    </article>

    <article class="abs item" style="top:240px">
      <h3 class="abs item-title">SHOP EQUIPMENT/TOOLS * PORK PROCESSING ITEMS</h3>
      <div class="abs thumb"><div role="img" aria-label="Yellow crawler loader tractor"></div></div>
      <div class="abs live">LIVE ON-SITE AUCTION</div>
      <div class="abs meta" style="top:51px"><b>Begins:</b> Saturday, March 16, 2013 at 10:00 AM EDT</div>
      <div class="abs meta" style="top:71px"><b>Location:</b> 5183 Larkin Road Fenwick, KY 40011</div>
      <p class="abs desc">Kestrel BS3F High Lift, 600 Series Halden tractor w/Brantley Loader, Dune buggy, 1207 RM Cutditioner: SHOP &amp; MISCELLANIOUS &amp; PORK PROCESSING ITEMS.</p>
      <div class="abs links">
        <div class="link-row" style="top:3px"><svg width="24" height="22" viewBox="0 0 24 22"><rect x="1" y="2" width="22" height="19" fill="#fff" stroke="#5a8fc8" stroke-width="1.5"/><rect x="1" y="2" width="22" height="5" fill="#5a8fc8"/><path d="M4 10h16M4 14h16M4 18h16M9 7v14M15 7v14" stroke="#9bbde0"/></svg>Details</div>
        <div class="link-row" style="top:46px"><svg width="24" height="22" viewBox="0 0 24 22"><rect x="1" y="6" width="22" height="15" rx="2" fill="#2a2f3a"/><rect x="7" y="2" width="9" height="5" fill="#2a2f3a"/><circle cx="12" cy="13" r="5" fill="#3f7fc0" stroke="#ccc"/></svg>Photo Galleries</div>
      </div>
      <div class="abs rule"></div>
    </article>

    <article class="abs item" style="top:425px">
      <h3 class="abs item-title">SHOP EQUIPMENT/TOOLS * PORK PROCESSING ITEMS</h3>
      <div class="abs thumb"><div role="img" aria-label="Yellow crawler loader tractor"></div></div>
      <div class="abs live">LIVE ON-SITE AUCTION</div>
      <div class="abs meta" style="top:51px"><b>Begins:</b> Saturday, March 16, 2013 at 10:00 AM EDT</div>
      <div class="abs meta" style="top:71px"><b>Location:</b> 5183 Larkin Road Fenwick, KY 40011</div>
      <p class="abs desc">Kestrel BS3F High Lift, 600 Series Halden tractor w/Brantley Loader, Dune buggy, 1207 RM Cutditioner: SHOP &amp; MISCELLANIOUS &amp; PORK PROCESSING ITEMS.</p>
      <div class="abs links">
        <div class="link-row" style="top:3px"><svg width="24" height="22" viewBox="0 0 24 22"><rect x="1" y="2" width="22" height="19" fill="#fff" stroke="#5a8fc8" stroke-width="1.5"/><rect x="1" y="2" width="22" height="5" fill="#5a8fc8"/><path d="M4 10h16M4 14h16M4 18h16M9 7v14M15 7v14" stroke="#9bbde0"/></svg>Details</div>
        <div class="link-row" style="top:46px"><svg width="24" height="22" viewBox="0 0 24 22"><rect x="1" y="6" width="22" height="15" rx="2" fill="#2a2f3a"/><rect x="7" y="2" width="9" height="5" fill="#2a2f3a"/><circle cx="12" cy="13" r="5" fill="#3f7fc0" stroke="#ccc"/></svg>Photo Galleries</div>
      </div>
    </article>

    <div class="abs view-more">View more</div>
  </main>

  <aside class="abs widget" style="top:499px;height:197px">
    <div class="widget-head">Featured Auctions</div>
    <div class="abs fa-link">TRACTOR * HI LIFT * MACHINERY</div>
    <div class="abs fa-thumb" role="img" aria-label="Yellow crawler loader tractor"></div>
    <div class="abs fa-text"><b>Saturday March 16,<br>2013 at 10:00 AM EDT</b><br><span style="display:block;margin-top:8px">Larkin Road<br>Fenwick, KY 40011</span></div>
    <div class="read-more" style="top:161px">read more</div>
  </aside>

  <aside class="abs widget" style="top:717px;height:197px">
    <div class="widget-head">Featured Video</div>
    <div class="abs video" role="img" aria-label="Video still of a brick country house">
      <div class="abs play"><svg width="60" height="42" viewBox="0 0 60 42"><path d="M23 11l16 10-16 10z" fill="#fff"/></svg></div>
      <div class="abs controls"><span>&#9654;</span><span>00:00</span><span class="progress"></span><span>00:00</span><span style="margin-left:auto">&#9646;&#9646;</span></div>
    </div>
  </aside>

  <aside class="abs widget" style="top:935px;height:197px">
    <div class="widget-head">Client Testimonials</div>
    <p class="abs testimonial">simply dummy text of the printing and typesetting industry. Lorem Ipsum has been the industry's standard dummy text ever since the 1500s, when an unknown printer took a galley of type and scrambled it to make a type specimen book.</p>
    <div class="read-more" style="top:163px">read more</div>
  </aside>

  <footer>
    <div class="abs footer-nav">Home<span>|</span>Auctions<span>|</span>Online Auctions<span>|</span>About Us<span>|</span>Contact Us</div>
    <div class="abs copyright">Copyright (C) Whitcombe's Auction . 2013.&nbsp; All Rights Reserved</div>
    <div class="abs horse" role="img" aria-label="Horse head emblem"></div>
    <div class="abs foot-brand">WHITCOMBE'S AUCTION<br>MART LTD.<i></i></div>
    <span class="abs card" style="left:886px;width:40px;background:#1a3f8f"></span>
    <span class="abs card" style="left:930px;width:40px;background:#d8262e"></span>
    <span class="abs card" style="left:974px;width:40px;background:#2a6fb5"></span>
    <span class="abs card" style="left:1018px;width:71px;background:#e8eef5"></span>
  </footer>
</div>
</body>
</html>
```